MIGRAINE BOX DESIGN

The template will be our newest version, it has a backer board allowing for more space and all.

I uploaded our previous box as an example for the new version.

Ill let you lay it out and well go from there.

```html
<!DOCTYPE html>
<html lang="en">
<head>
<meta charset="utf-8">
<title>Migraine Roll-On Box – Dieline</title>
<link rel="stylesheet" href="https://fonts.googleapis.com/css2?family=Archivo+Black&family=Fira+Sans+Extra+Condensed:wght@400;600;700;800&display=swap">
<style>
  :root{
    --navy:#231c66;
    --navy-deep:#1d1858;
    --blue:#3a64ae;
    --blue-light:#5a9ad2;
    --brand-red:#d9381e;
    --ink:#1a1a1a;
    --fold-green:#7cc242;
    --paper:#ffffff;
    --mark-tint:#dfe6f1;
  }
  html,body{margin:0;padding:0;width:1200px;height:849px;overflow:hidden;background:var(--paper);}
  .dieline{display:block;width:1200px;height:849px;}
  .brand{font-family:"Fira Sans Extra Condensed",sans-serif;font-weight:800;fill:var(--brand-red);}
  .product-line{font-family:"Fira Sans Extra Condensed",sans-serif;font-weight:700;fill:var(--ink);font-size:12.5px;}
  .headline{font-family:"Archivo Black",sans-serif;}
  .tagline{font-family:"Fira Sans Extra Condensed",sans-serif;font-weight:600;font-size:9.5px;fill:var(--paper);}
  .tagline-dark{font-family:"Fira Sans Extra Condensed",sans-serif;font-weight:700;font-size:8.6px;fill:var(--navy-deep);}
  .fine{font-family:"Fira Sans Extra Condensed",sans-serif;font-weight:400;font-size:6.2px;fill:var(--ink);}
  .fine-bold{font-family:"Fira Sans Extra Condensed",sans-serif;font-weight:700;font-size:6.2px;fill:var(--ink);}
  .label{font-weight:700;}
  .cut{fill:none;stroke:var(--ink);stroke-width:1;}
  .fold{fill:none;stroke:var(--fold-green);stroke-width:1;}
  .compliance-mark{fill:var(--mark-tint);}
  .hang-hole{fill:var(--paper);stroke:var(--ink);stroke-width:1;}
</style>
</head>
<body>
<svg class="dieline" viewBox="0 0 1200 849" xmlns="http://www.w3.org/2000/svg">
  <defs>
    <linearGradient id="panel-blue" x1="0" y1="0" x2="1" y2="1">
      <stop offset="0" stop-color="#2a2f7c"/>
      <stop offset="0.42" stop-color="#3a64ae"/>
      <stop offset="0.52" stop-color="#5a9ad2"/>
      <stop offset="0.75" stop-color="#2d3b8e"/>
      <stop offset="1" stop-color="#241d68"/>
    </linearGradient>
    <linearGradient id="end-blue" x1="0" y1="0" x2="0" y2="1">
      <stop offset="0" stop-color="#2a2378"/>
      <stop offset="0.5" stop-color="#4c85c4"/>
      <stop offset="1" stop-color="#241c66"/>
    </linearGradient>
    <linearGradient id="headline-silver" x1="0" y1="0" x2="0" y2="1">
      <stop offset="0" stop-color="#ffffff"/>
      <stop offset="0.55" stop-color="#f1f1f4"/>
      <stop offset="1" stop-color="#a9a9b3"/>
    </linearGradient>
    <linearGradient id="headline-navy" x1="0" y1="0" x2="1" y2="0">
      <stop offset="0" stop-color="#3b5bb0"/>
      <stop offset="1" stop-color="#1d1858"/>
    </linearGradient>
    <linearGradient id="ice-field" x1="0" y1="0" x2="1" y2="1">
      <stop offset="0" stop-color="#f4f9fd"/>
      <stop offset="1" stop-color="#e1eff9"/>
    </linearGradient>
    <clipPath id="band-clip">
      <path d="M52,242 H1148 Q1170,242 1170,264 V611 Q1170,633 1148,633 H52 Q30,633 30,611 V264 Q30,242 52,242 Z"/>
    </clipPath>
  </defs>

  <!-- Flaps -->
  <g class="flaps">
    <path class="cut" fill="#fff" d="M497,136 V112 Q497,87 522,87 H572 Q597,87 597,112 V136"/>
    <rect x="495" y="136" width="104" height="106" fill="#fff"/>
    <path class="cut" d="M495,242 V136 H522 M572,136 H599 V242"/>
    <path class="fold" d="M522,136 H572"/>
    <path class="cut" d="M497,737 V763 Q497,788 522,788 H572 Q597,788 597,763 V737"/>
    <rect x="495" y="633" width="104" height="104" fill="#fff"/>
    <path class="cut" d="M495,633 V737 H522 M572,737 H599 V633"/>
    <path class="fold" d="M522,737 H572"/>
    <path class="cut" d="M394,242 V222 L399,217 V197 H483 L486,233 L495,242"/>
    <path class="cut" d="M702,242 V222 L697,217 V197 H611 L608,233 L599,242"/>
    <path class="cut" d="M394,633 V653 L399,658 V678 H483 L486,642 L495,633"/>
    <path class="cut" d="M702,633 V653 L697,658 V678 H611 L608,642 L599,633"/>

    <text class="brand" x="547" y="197" font-size="24" text-anchor="middle">TORVEN'S</text>
    <text class="product-line" x="547" y="211" text-anchor="middle">THC PAIN RELIEF</text>
    <text class="product-line" x="547" y="224" text-anchor="middle">ROLL ON STICK</text>

    <text class="brand" x="547" y="686" font-size="24" text-anchor="middle">TORVEN'S</text>
    <text class="product-line" x="547" y="699" text-anchor="middle">THC PAIN RELIEF</text>
    <text class="product-line" x="547" y="712" text-anchor="middle">ROLL ON STICK</text>
  </g>

  <!-- Main band -->
  <g class="band" clip-path="url(#band-clip)">
    <rect class="backer-end" x="30" y="242" width="85" height="391" fill="url(#end-blue)" role="img" aria-label="Navy backer end with faint leaf pattern"/>
    <rect class="backer-white" x="115" y="242" width="74" height="391" fill="#fff"/>
    <rect class="panel-back" x="189" y="242" width="205" height="391" fill="url(#panel-blue)" role="img" aria-label="Blue gradient panel with faint leaf pattern"/>
    <rect class="panel-side" x="394" y="242" width="308" height="391" fill="#fff"/>
    <rect class="panel-front-blue" x="702" y="242" width="205" height="391" fill="url(#panel-blue)" role="img" aria-label="Blue gradient panel with faint leaf pattern"/>
    <rect class="backer-ice" x="907" y="242" width="178" height="391" fill="url(#ice-field)" role="img" aria-label="Pale ice-blue field with scattered leaf pattern"/>
    <rect class="backer-end" x="1085" y="242" width="85" height="391" fill="url(#end-blue)" role="img" aria-label="Navy backer end with faint leaf pattern"/>
  </g>
  <path class="cut" d="M52,242 H394 M702,242 H1148 Q1170,242 1170,264 V611 Q1170,633 1148,633 H702 M394,633 H52 Q30,633 30,611 V264 Q30,242 52,242"/>
  <rect class="fold" x="394" y="242" width="308" height="391"/>
  <path class="fold" d="M495,242 V633 M599,242 V633"/>

  <path class="hang-hole" d="M71,420 a6,6 0 0 1 12,0 a18,18 0 1 1 -12,0 Z"/>
  <path class="hang-hole" d="M1117,420 a6,6 0 0 1 12,0 a18,18 0 1 1 -12,0 Z"/>

  <!-- Backer white: brand -->
  <text class="brand" transform="translate(177,437) rotate(-90)" font-size="36" text-anchor="middle" textLength="145" lengthAdjust="spacingAndGlyphs">TORVEN'S</text>

  <!-- Back blue panel -->
  <rect class="compliance-mark" x="208" y="259" width="26" height="26" rx="3"/>
  <text class="headline" transform="translate(301,437) rotate(-90)" font-size="70" fill="url(#headline-silver)" text-anchor="middle" textLength="320" lengthAdjust="spacingAndGlyphs">MIGRAINE</text>
  <text class="tagline" transform="translate(318,437) rotate(-90)" text-anchor="middle" textLength="317" lengthAdjust="spacingAndGlyphs">FORMULATED TO HELP DECREASE THE PAIN TENSION AND INTENSITY ASSOCIATED</text>
  <text class="tagline" transform="translate(333,437) rotate(-90)" text-anchor="middle" textLength="135" lengthAdjust="spacingAndGlyphs">WITH HEADACHES AND MIGRAINES</text>

  <!-- Warning side panel -->
  <g class="warnings" transform="translate(489,247) rotate(90)">
    <text class="fine" x="0" y="6" textLength="360" lengthAdjust="spacingAndGlyphs"><tspan class="label">WARNING:</tspan> THIS PRODUCT IS FOR USE BY INDIVIDUALS 21 YEARS OF AGE OR OLDER. IT IS ILLEGAL TO DRIVE A MOTOR VEHICLE WHILE UNDER THE</text>
    <text class="fine" x="0" y="14">INFLUENCE OF MARIJUANA. ACTIVATION TIME: 10-60 MINUTES</text>
    <text class="fine" x="0" y="22" textLength="360" lengthAdjust="spacingAndGlyphs"><tspan class="label">WARNING:</tspan> THIS PRODUCT IS FOR USE BY INDIVIDUALS 21 YEARS OF AGE OR OLDER. IT IS ILLEGAL TO DRIVE A MOTOR VEHICLE WHILE UNDER THE</text>
    <text class="fine" x="0" y="30">INFLUENCE OF MARIJUANA. ACTIVATION TIME: 10-60 MINUTES</text>
    <rect x="1" y="35" width="373" height="21" fill="none" stroke="#1a1a1a" stroke-width="0.8"/>
    <text class="fine-bold" x="4" y="43" textLength="366" lengthAdjust="spacingAndGlyphs">WARNING: THIS PRODUCT IS FOR USE BY INDIVIDUALS 21 YEARS OF AGE OR OLDER. IT IS ILLEGAL TO DRIVE A MOTOR VEHICLE WHILE</text>
    <text class="fine-bold" x="4" y="51">UNDER THE INFLUENCE OF MARIJUANA. ACTIVATION TIME: 10-60 MINUTES</text>
    <text class="fine-bold" x="0" y="64">THE ACTUAL VALUE OF REPORTED CANNABINOIDS MAY VARY FROM THE REPORTED VALUE BY +/- 15%</text>
    <text class="fine-bold" x="0" y="72">KEEP OUT OF REACH OF CHILDREN. NATIONAL POISON CONTROL CENTER 1 800 555 0199</text>
    <text class="fine-bold" x="0" y="80">MADE IN A MARIJUANA FACILITY. DISTRIBUTED BY FENNICK ROW CO. 220 QUARRY BEND RD, ALDER BAY, MI 49000</text>
    <text class="fine-bold" x="0" y="88">www.FENNICKROWCO.com www.TORVENSPRODUCTS.com NET WT. 0.50 OZ</text>
  </g>

  <!-- Front panel -->
  <text class="brand" x="547" y="276" font-size="24" text-anchor="middle">TORVEN'S</text>
  <text class="headline" transform="translate(531,436) rotate(90)" font-size="66" fill="url(#headline-navy)" text-anchor="middle" textLength="296" lengthAdjust="spacingAndGlyphs">MIGRAINE</text>
  <text class="tagline-dark" transform="translate(517,436) rotate(90)" text-anchor="middle" textLength="296" lengthAdjust="spacingAndGlyphs">FORMULATED TO HELP DECREASE THE PAIN TENSION AND INTENSITY ASSOCIATED</text>
  <text class="tagline-dark" transform="translate(506,436) rotate(90)" text-anchor="middle" textLength="127" lengthAdjust="spacingAndGlyphs">WITH HEADACHES AND MIGRAINES</text>
  <rect class="compliance-mark" x="558" y="597" width="27" height="27" rx="3"/>

  <!-- Ingredients side panel -->
  <g class="ingredients" transform="translate(697,248) rotate(90)">
    <text class="fine" x="0" y="7.5" textLength="364" lengthAdjust="spacingAndGlyphs"><tspan class="label">ORGANIC INGREDIENTS:</tspan> BEESWAX, SHEA BUTTER, COCONUT OIL, GRAPESEED OIL, JOJOBA OIL, THC OIL (CANNABIS EXTRACT), PURE CBD AND PURE</text>
    <text class="fine" x="0" y="17.5" textLength="364" lengthAdjust="spacingAndGlyphs">CBG (HEMP EXTRACT), THERAPEUTIC GRADE ESSENTIAL OILS (INCLUDING BUT NOT LIMITED TO); MINT PEPPERMINT CAMPHOR, LAVENDER, PEPPERMINT</text>
    <text class="fine" x="0" y="28.5" textLength="364" lengthAdjust="spacingAndGlyphs">INDIAN OIL &amp; WILD CHAMOMILE) *BLUE COLOR OCCURS NATURALLY DURING DISTILLATION WHEN THE PLANT COMPONENTS REACT WITH HEAT &amp; MAY</text>
    <text class="fine" x="0" y="38.5">VARY IN INTENSITY</text>
    <text class="fine" x="0" y="50.5"><tspan class="label">HOW TO USE:</tspan> MASSAGE ONTO TEMPLES, FOREHEAD, AND BACK OF NECK FOR MAXIMUM EFFECT USE DAILY</text>
    <text class="fine" x="0" y="59.5">OR RE-APPLY AS OFTEN AS NEEDED. FOR TOPICAL USE ONLY.</text>
    <text class="fine" x="0" y="70.5"><tspan class="label">AROMATHERAPEUTIC:</tspan> PEPPERMINT WITH CHAMOMILE AND LAVENDER UNDERTONE</text>
    <text class="fine" x="0" y="81.5"><tspan class="label">CONSISTENCY:</tspan> LIGHT, SMOOTH &amp; FAST ABSORBING WITH COOLING SENSATION</text>
    <text class="fine" x="0" y="91.5"><tspan class="label">PURPOSE:</tspan> NATURAL REMEDY FOR HEADACHE &amp; MIGRAINE PAIN</text>
  </g>
  <text class="brand" transform="translate(611,577) rotate(90)" font-size="25" text-anchor="middle" textLength="77" lengthAdjust="spacingAndGlyphs">TORVEN'S</text>

  <!-- Right blue panel -->
  <text class="headline" transform="translate(798,437) rotate(90)" font-size="64" fill="url(#headline-silver)" text-anchor="middle" textLength="320" lengthAdjust="spacingAndGlyphs">MIGRAINE</text>
  <text class="tagline" transform="translate(776,437) rotate(90)" text-anchor="middle" textLength="317" lengthAdjust="spacingAndGlyphs">FORMULATED TO HELP DECREASE THE PAIN TENSION AND INTENSITY ASSOCIATED</text>
  <text class="tagline" transform="translate(762,437) rotate(90)" text-anchor="middle" textLength="136" lengthAdjust="spacingAndGlyphs">WITH HEADACHES AND MIGRAINES</text>
  <rect class="compliance-mark" x="860" y="588" width="27" height="27" rx="3"/>

  <!-- Backer ice panel: brand -->
  <text class="brand" transform="translate(965,436) rotate(90)" font-size="58" text-anchor="middle" textLength="238" lengthAdjust="spacingAndGlyphs">TORVEN'S</text>
</svg>
</body>
</html>
```